Soccer Training Plan template design

We are seeking a bespoke soccer training plan template design that can be easily used by staff to create training plan diagrams.

Currently we use third party applications for this, but this limits us to 'in-house' use due to copyright of the various application template design. We wish to have our own to allow us to publish externally.

The template should allow the user to select field options (as shown on right hand side in example), equipment, players, arrows, etc. It should also give opportunity to add text to the template before exporting the finished diagram.

Attached is a quick mock-up made in powerpoint, however there are many examples online of similar templates if you search for 'soccer training diagram'.

We would like the template to be usable on a white background (as per example) where green external lines for the soccer pitch should be used; but also on a coloured background - for this white external lines should be used.

Essential Element Requirements:

Pitch options: Square, Rectangle, Circle, Full Pitch, Half Pitch, Penalty Box (1/3 of Pitch), Centre Pitch (1/3 of Pitch)

Player Options: Outfield Players, Goalkeepers, Neutral Options. (multiple colour options, or colour should be changeable by user)

Lines: Solid, Dashed and Dotted (both solid colour, and 50% transparency)

Arrows: Solid Straight, Dashed Straight, Dashed Wavy, Dotted Straight and Dotted Wavy (both solid colour, and 50% transparency)*

*note - for the straight arrows (ie, not wavy), it would be preferable if there was an option to also curve these, so that the user can represent a curved movement of a player or ball in their diagrams

Equipment: Soccer Goals (Large and Small), Soccer Ball, Mannequin, Pole, Cone, Marker, Hurdle

Thanks for taking the time to review our project, and we look forward to receiving your designs!

Industry/Entity Type

Sport, Soccer, Football

Font styles to use
Sans Serif

Colors
00AB8E
00BBA5
67D7C9
C6EFE9
E9F9F6

Requirements
Must have
• Essential Element Requirements: Pitch options: Square, Rectangle, Circle, Full Pitch, Half Pitch, Penalty Box (1/3 of Pitch), Centre Pitch (1/3 of Pitch) Player Options: Outfield Players, Goalkeepers, Neutral Options. (multiple colour options, or colour should be changeable by user) Lines: Solid, Dashed and Dotted (both solid colour, and 50% transparency) Arrows: Solid Straight, Dashed Straight, Dashed Wavy, Dotted Straight and Dotted Wavy (both solid colour, and 50% transparency)* *note - for the straight arrows (ie, not wavy), it would be preferable if there was an option to also curve these, so that the user can represent a curved movement of a player or ball in their diagrams Equipment: Soccer Goals (Large and Small), Soccer Ball, Mannequin, Pole, Cone, Marker, Hurdle

```html
<!DOCTYPE html>
<html lang="en">
<head>
<meta charset="utf-8">
<title>Soccer Training Plan Template</title>
<link rel="stylesheet" href="https://fonts.googleapis.com/css2?family=Montserrat:wght@500&display=swap">
<style>
  :root {
    --pitch-green: #12a04a;
    --field-green: #0e9444;
    --line-white: #ffffff;
    --ink: #000000;
    --red: #ed1c24;
    --grey: #808080;
    --pink: #f3868c;
    --blue: #0f75bc;
    --lime: #8dc63f;
    --purple: #7f3f98;
    --neutral: #999999;
    --cone: #f9b03c;
    --hurdle: #f05a28;
    --equipment: #555555;
    --red-light: #f08b8f;
    --blue-light: #7ba7c8;
    --lime-light: #b5cf94;
    --goal-fill: #e3e3e3;
  }
  html, body { margin: 0; padding: 0; overflow: hidden; background: #fff; }
  .sheet { display: block; width: 1200px; height: 2230px; }
  .pitch-lines { fill: none; stroke-width: 3; }
  .pitch-lines .spot { stroke: none; fill: currentColor; }
  .pitches-white-bg { color: var(--pitch-green); stroke: var(--pitch-green); }
  .pitches-green-bg { color: var(--line-white); stroke: var(--line-white); }
  .field-band { fill: var(--field-green); }
  .line { fill: none; stroke-width: 3; }
  .dashed { stroke-dasharray: 9 6; }
  .dotted { stroke-dasharray: 2 7; stroke-linecap: round; }
  .player-label { font-family: "Montserrat", sans-serif; font-weight: 500; fill: #fff; text-anchor: middle; dominant-baseline: central; }
</style>
</head>
<body>
<svg class="sheet" viewBox="0 0 1386 2576" xmlns="http://www.w3.org/2000/svg">
  <defs>
    <g id="pitch-set" class="pitch-lines">
      <!-- Full pitch -->
      <rect x="67" y="101" width="396" height="619"/>
      <rect x="142" y="101" width="246" height="99"/>
      <rect x="209" y="101" width="112" height="33"/>
      <circle class="spot" cx="265" cy="162" r="2.5"/>
      <path d="M210 200 A67 67 0 0 0 320 200"/>
      <line x1="67" y1="410" x2="463" y2="410"/>
      <circle cx="265" cy="410" r="67"/>
      <circle class="spot" cx="265" cy="410" r="4"/>
      <rect x="142" y="621" width="246" height="99"/>
      <rect x="209" y="687" width="112" height="33"/>
      <circle class="spot" cx="265" cy="659" r="2.5"/>
      <path d="M210 621 A67 67 0 0 1 320 621"/>
      <!-- Half pitch -->
      <rect x="522" y="101" width="395" height="308"/>
      <rect x="597" y="101" width="246" height="99"/>
      <rect x="663" y="101" width="112" height="33"/>
      <circle class="spot" cx="719" cy="162" r="2.5"/>
      <path d="M664 200 A67 67 0 0 0 774 200"/>
      <path d="M652 409 A67 67 0 0 1 786 409"/>
      <!-- Centre third -->
      <rect x="521" y="437" width="395" height="206"/>
      <line x1="521" y1="540" x2="916" y2="540"/>
      <circle cx="718" cy="540" r="67"/>
      <circle class="spot" cx="718" cy="540" r="4"/>
      <!-- Penalty third -->
      <rect x="521" y="672" width="395" height="206"/>
      <rect x="596" y="672" width="246" height="99"/>
      <rect x="662" y="672" width="112" height="33"/>
      <circle class="spot" cx="718" cy="733" r="2.5"/>
      <path d="M663 771 A67 67 0 0 0 773 771"/>
      <!-- Free areas -->
      <rect x="958" y="101" width="209" height="209"/>
      <rect x="958" y="362" width="395" height="205"/>
      <circle cx="1088" cy="749" r="129"/>
    </g>
    <path id="wave" d="M430 0 C455 0 470 -18 487 -18 C505 -18 505 8 525 8 C545 8 545 -18 563 -18 C578 -18 580 -2 590 0"/>
  </defs>

  <!-- Pitch options on white -->
  <use href="#pitch-set" class="pitches-white-bg"/>

  <!-- Pitch options on coloured background -->
  <rect class="field-band" x="0" y="955" width="1386" height="930"/>
  <use href="#pitch-set" class="pitches-green-bg" transform="translate(0 926)"/>

  <!-- Lines -->
  <g class="line-options">
    <line class="line" stroke="var(--ink)" x1="63" y1="1962" x2="376" y2="1962"/>
    <line class="line" stroke="var(--red)" x1="63" y1="1996" x2="376" y2="1996"/>
    <line class="line dashed" stroke="var(--ink)" x1="63" y1="2030" x2="376" y2="2030"/>
    <line class="line dotted" stroke="var(--ink)" x1="63" y1="2063" x2="376" y2="2063"/>
    <line class="line" stroke="var(--grey)" x1="63" y1="2107" x2="376" y2="2107"/>
    <line class="line" stroke="var(--pink)" x1="63" y1="2140" x2="376" y2="2140"/>
    <line class="line dashed" stroke="var(--grey)" x1="63" y1="2174" x2="376" y2="2174"/>
    <line class="line dotted" stroke="var(--grey)" x1="63" y1="2207" x2="376" y2="2207"/>
  </g>

  <!-- Straight arrows -->
  <g class="arrow-options">
    <line class="line" stroke="var(--ink)" x1="63" y1="2260" x2="364" y2="2260"/><path d="M362 2252 L376 2260 L362 2268Z" fill="var(--ink)"/>
    <line class="line" stroke="var(--red)" x1="63" y1="2294" x2="364" y2="2294"/><path d="M362 2286 L376 2294 L362 2302Z" fill="var(--red)"/>
    <line class="line dashed" stroke="var(--ink)" x1="63" y1="2328" x2="364" y2="2328"/><path d="M362 2320 L376 2328 L362 2336Z" fill="var(--ink)"/>
    <line class="line dotted" stroke="var(--ink)" x1="63" y1="2362" x2="364" y2="2362"/><path d="M362 2354 L376 2362 L362 2370Z" fill="var(--ink)"/>
    <line class="line" stroke="var(--grey)" x1="63" y1="2414" x2="364" y2="2414"/><path d="M362 2406 L376 2414 L362 2422Z" fill="var(--grey)"/>
    <line class="line" stroke="var(--pink)" x1="63" y1="2448" x2="364" y2="2448"/><path d="M362 2440 L376 2448 L362 2456Z" fill="var(--pink)"/>
    <line class="line dashed" stroke="var(--grey)" x1="63" y1="2482" x2="364" y2="2482"/><path d="M362 2474 L376 2482 L362 2490Z" fill="var(--grey)"/>
    <line class="line dotted" stroke="var(--grey)" x1="63" y1="2516" x2="364" y2="2516"/><path d="M362 2508 L376 2516 L362 2524Z" fill="var(--grey)"/>
  </g>

  <!-- Wavy arrows -->
  <g class="wavy-arrows">
    <g transform="translate(0 2207)"><use href="#wave" class="line" stroke="var(--ink)"/><path d="M588 -8 L602 0 L588 8Z" fill="var(--ink)"/></g>
    <g transform="translate(0 2246)"><use href="#wave" class="line" stroke="var(--red)"/><path d="M588 -8 L602 0 L588 8Z" fill="var(--red)"/></g>
    <g transform="translate(0 2294)"><use href="#wave" class="line dashed" stroke="var(--ink)"/><path d="M588 -8 L602 0 L588 8Z" fill="var(--ink)"/></g>
    <g transform="translate(0 2340)"><use href="#wave" class="line dotted" stroke="var(--ink)"/><path d="M588 -8 L602 0 L588 8Z" fill="var(--ink)"/></g>
    <g transform="translate(0 2387)"><use href="#wave" class="line" stroke="var(--grey)"/><path d="M588 -8 L602 0 L588 8Z" fill="var(--grey)"/></g>
    <g transform="translate(0 2424)"><use href="#wave" class="line" stroke="var(--pink)"/><path d="M588 -8 L602 0 L588 8Z" fill="var(--pink)"/></g>
    <g transform="translate(0 2472)"><use href="#wave" class="line dashed" stroke="var(--grey)"/><path d="M588 -8 L602 0 L588 8Z" fill="var(--grey)"/></g>
    <g transform="translate(0 2520)"><use href="#wave" class="line dotted" stroke="var(--grey)"/><path d="M588 -8 L602 0 L588 8Z" fill="var(--grey)"/></g>
  </g>

  <!-- Equipment -->
  <g class="equipment">
    <line x1="518" y1="1985" x2="518" y2="2140" stroke="var(--equipment)" stroke-width="4"/>
    <path d="M510 2138 H526 L531 2148 H505Z" fill="var(--equipment)"/>
    <path d="M583 1968 L605 2022 H561Z" fill="var(--cone)"/>
    <path d="M627 2015 H650 L655 2022 H622Z" fill="var(--cone)"/>
    <path d="M680 2022 V2002 Q680 1995 687 1995 H722 Q729 1995 729 2002 V2022" fill="none" stroke="var(--hurdle)" stroke-width="4"/>
    <circle cx="583" cy="2060" r="12" fill="var(--equipment)"/>
    <rect x="558" y="2055" width="48" height="10" fill="var(--equipment)"/>
    <circle cx="639" cy="2046" r="9" fill="var(--equipment)"/>
    <path d="M623 2058 H655 L639 2082Z" fill="var(--equipment)"/>
    <circle cx="704" cy="2060" r="17" fill="var(--cone)"/>
    <circle cx="704" cy="2060" r="10" fill="none" stroke="var(--hurdle)" stroke-width="4"/>
    <circle cx="583" cy="2108" r="10" fill="var(--equipment)"/>
    <circle cx="583" cy="2143" r="10" fill="var(--red)"/>
    <path d="M628 2095 L650 2117 M650 2095 L628 2117" stroke="var(--red)" stroke-width="3"/>
    <circle cx="639" cy="2143" r="9" fill="none" stroke="var(--red)" stroke-width="3"/>
    <g class="ball">
      <circle cx="709" cy="2127" r="29" fill="#fff" stroke="var(--ink)" stroke-width="3"/>
      <path d="M709 2116 L719 2123 L715 2135 L703 2135 L699 2123Z" fill="var(--ink)"/>
      <path d="M700 2099 L718 2099 L716 2106 L702 2106Z M683 2118 L689 2133 L682 2138 L681 2124Z M735 2118 L737 2124 L736 2138 L729 2133Z M697 2152 L709 2147 L721 2152 L716 2155 L702 2155Z" fill="var(--ink)"/>
      <path d="M709 2116 V2106 M719 2123 L735 2118 M715 2135 L721 2152 M703 2135 L697 2152 M699 2123 L683 2118" stroke="var(--ink)" stroke-width="2"/>
    </g>
  </g>

  <!-- Players -->
  <g class="players">
    <circle cx="816" cy="1992" r="21" fill="var(--neutral)"/><text class="player-label" x="816" y="1993" font-size="28">N</text>
    <circle cx="873" cy="1992" r="21" fill="var(--red)"/><text class="player-label" x="873" y="1993" font-size="28">1</text>
    <circle cx="929" cy="1992" r="21" fill="var(--blue)"/><text class="player-label" x="929" y="1993" font-size="28">2</text>
    <circle cx="985" cy="1992" r="21" fill="var(--lime)"/><text class="player-label" x="985" y="1993" font-size="28">3</text>
    <circle cx="816" cy="2046" r="21" fill="var(--purple)"/><text class="player-label" x="816" y="2047" font-size="19">GK</text>
    <circle cx="873" cy="2046" r="21" fill="var(--red)"/>
    <circle cx="929" cy="2046" r="21" fill="var(--blue)"/>
    <circle cx="985" cy="2046" r="21" fill="var(--lime)"/>
    <path d="M852 2105 A21 21 0 0 1 894 2105Z" fill="var(--red)"/>
    <path d="M908 2105 A21 21 0 0 1 950 2105Z" fill="var(--blue)"/>
    <path d="M964 2105 A21 21 0 0 1 1006 2105Z" fill="var(--lime)"/>
    <circle cx="873" cy="2147" r="21" fill="none" stroke="var(--red)" stroke-width="4"/>
    <circle cx="929" cy="2147" r="21" fill="none" stroke="var(--blue)" stroke-width="4"/>
    <circle cx="985" cy="2147" r="21" fill="none" stroke="var(--lime)" stroke-width="4"/>
    <circle cx="873" cy="2203" r="21" fill="var(--red-light)"/>
    <circle cx="929" cy="2203" r="21" fill="var(--blue-light)"/>
    <circle cx="985" cy="2203" r="21" fill="var(--lime-light)"/>
  </g>

  <!-- Goals -->
  <g class="goals">
    <rect x="1065" y="1980" width="249" height="105" fill="var(--goal-fill)" role="img" aria-label="Large soccer goal with net, front view"/>
    <rect x="1065" y="2127" width="138" height="75" fill="var(--goal-fill)" role="img" aria-label="Small soccer goal with net, front view"/>
    <rect x="1065" y="2240" width="292" height="73" fill="var(--goal-fill)" role="img" aria-label="Large soccer goal with net, top view"/>
    <rect x="1065" y="2328" width="166" height="72" fill="var(--goal-fill)" role="img" aria-label="Small soccer goal with net, top view"/>
  </g>
</svg>
</body>
</html>
```